Velloria Flowers Florist Flyer

We are requiring a flyer that advertises and promotes our new business. We specialise in weddings and events but would also like to branch out to corporates and an online subscription. Our brand is feminine/romantic with a touch of elegance and luxury. Our main colour schemes are white, black, gold and pale pink. Instagram: Velloria_flowers and website www.velloriaflowers.com.au
Target Market(s)
brides to be, females
Industry/Entity Type
Florist
Font styles to use
Sans Serif
Script
Other font styles liked:
- The Carpenter
Colors
ffffff
000000
333333
Requirements
Must have
- Feminine/romantic feel, through use of theme colours and elegant font
- our contact details Ph: 0429518064
- email address: contactus@velloriaflowers.com.au
Nice to have
- a description of us willing to work with clients to create their dream wedding flowers. That we offer consultations and no obligation quotes.

```html
<!DOCTYPE html>
<html lang="en">
<head>
<meta charset="utf-8">
<title>Velloria Flowers Flyer</title>
<link rel="stylesheet" href="https://fonts.googleapis.com/css2?family=Montserrat:wght@500;700;800&family=Great+Vibes&display=swap">
<style>
  :root {
    --backdrop: #4a4a4a;
    --paper-pink: #fcdde3;
    --ink: #111111;
    --photo-pink: #f3a9bf;
    --photo-warm: #f6c6a0;
    --photo-teal: #a9c4c2;
  }
  * { margin: 0; padding: 0; box-sizing: border-box; }
  html, body {
    width: 1200px; height: 800px; overflow: hidden;
    background: var(--backdrop);
    font-family: "Montserrat", Arial, sans-serif;
    color: var(--ink);
  }
  .canvas {
    width: 1200px; height: 800px;
    display: flex; align-items: center; justify-content: center;
  }
  .flyer {
    position: relative;
    width: 570px; height: 760px;
    background: var(--paper-pink);
    overflow: hidden;
  }
  .contact-email {
    position: absolute; top: 26px; left: 30px;
    font-size: 11px; font-weight: 700;
  }
  .contact-social {
    position: absolute; top: 44px; left: 30px;
    font-size: 11px; font-weight: 700;
  }
  .contact-phone {
    position: absolute; top: 58px; right: 30px;
    font-size: 12px; font-weight: 700;
  }
  .brand-name {
    position: absolute; top: 78px; left: 0; width: 100%;
    text-align: center;
    font-family: "Great Vibes", cursive;
    font-size: 50px; font-weight: 400; line-height: 64px;
  }
  .intro {
    position: absolute; top: 158px; left: 0; width: 100%;
    text-align: center; text-transform: uppercase;
    font-size: 10.5px; font-weight: 700; line-height: 19px; letter-spacing: 0.6px;
  }
  .bouquet-photo {
    position: absolute; top: 250px; left: 95px;
    width: 440px; height: 510px;
  }
  .headline {
    position: absolute; top: 300px; left: 0; width: 100%;
    text-align: center; text-transform: uppercase;
    font-size: 20px; font-weight: 800; letter-spacing: 2.5px; line-height: 26px;
  }
  .services {
    position: absolute; top: 585px; left: 50px; right: 40px;
    display: flex; justify-content: space-between;
    list-style: none;
    font-size: 17px; font-weight: 700; letter-spacing: 2px; text-transform: uppercase;
  }
  .website {
    position: absolute; top: 655px; left: 0; width: 100%;
    text-align: center;
    font-size: 28px; font-weight: 800; letter-spacing: 3px;
  }
</style>
</head>
<body>
<main class="canvas">
  <article class="flyer">
    <p class="contact-email">contactus@velloriaflowers.com.au</p>
    <p class="contact-social">Instagram: Velloria_flowers</p>
    <p class="contact-phone">Ph: 0429518064</p>

    <h1 class="brand-name">Velloria Flowers</h1>

    <p class="intro">
      Looking for flowers for a wedding or event?<br>
      We specialise in flowers for weddings and events.<br>
      No matter how big or small<br>
      we're here to create the best looking flowers<br>
      just for you.
    </p>

    <svg class="bouquet-photo" viewBox="0 0 440 510" preserveAspectRatio="none" role="img" aria-label="Photo of two hands holding a heart-shaped flower arrangement">
      <defs>
        <linearGradient id="photo-tones" x1="0" y1="0" x2="0" y2="1">
          <stop offset="0%" stop-color="var(--photo-pink)"/>
          <stop offset="45%" stop-color="var(--photo-warm)"/>
          <stop offset="75%" stop-color="var(--photo-teal)"/>
          <stop offset="100%" stop-color="var(--paper-pink)"/>
        </linearGradient>
      </defs>
      <rect x="0" y="0" width="440" height="510" fill="url(#photo-tones)"/>
    </svg>

    <h2 class="headline">Creating stunning flowers<br>for weddings and events</h2>

    <ul class="services">
      <li>Wedding</li>
      <li>Events</li>
      <li>Business</li>
      <li>Home</li>
    </ul>

    <p class="website">www.velloriaflowers.com.au</p>
  </article>
</main>
</body>
</html>
```